Business Cards for a Junk Removal Company

Hello,
We are looking to have business cards designed that are simple, bold, easy to read, and right to the point. Please see the attachments for our logo files. We want the card to be yellow on both sides ( Color code Yellow: #FFE01B). The logo text font is (Rockstar Extra Bold) and this is also in the files attached. Please make the text black for the logo. On the back side of the card, you can use white and black for text. Thank you in advance for your hard work!

Front of card-
Harbor Haul Away (logo)
Back of card-
Harbor Haul Away
Donate - Recycle - Dispose
555-271-8093
www.harborhaulaway.example
info@harborhaulaway.example

Industry/Entity Type

Junk removal

Contact Information for Business Card

FRONT OF CARD- Harbor Haul Away (logo) BACK OF CARD- Harbor Haul Away Donate - Recycle - Dispose 555-271-8093 www.harborhaulaway.example info@harborhaulaway.example

Font styles to use
Other font styles liked:
• Rockstar Extra Bold

Colors
FFF300
FFF600
FEFA6F
FFFEC7
FFFEE8

Requirements
Must have
• Must have color code Yellow: #FFE01B for the background of front and back of the card

```html
<!DOCTYPE html>
<html lang="en">
<head>
<meta charset="utf-8">
<title>Harbor Haul Away – Business Cards</title>
<link href="https://fonts.googleapis.com/css2?family=Montserrat:wght@500;800&display=swap" rel="stylesheet">
<style>
  :root {
    --backdrop: #333333;
    --brand-yellow: #F5D655;
    --ink: #1f1c1d;
    --paper: #ffffff;
  }
  * { margin: 0; padding: 0; box-sizing: border-box; }
  html, body {
    width: 1200px;
    height: 984px;
    overflow: hidden;
    background: var(--backdrop);
    font-family: "Montserrat", sans-serif;
  }
  .card {
    position: absolute;
    left: 215px;
    width: 770px;
    height: 440px;
    overflow: hidden;
    box-shadow: 0 6px 18px rgba(0,0,0,0.45);
  }
  .card-front {
    top: 32px;
    background: var(--brand-yellow);
    display: flex;
    align-items: center;
    justify-content: center;
  }
  .front-name {
    color: var(--paper);
    font-weight: 800;
    font-size: 56px;
    letter-spacing: 1px;
    text-transform: uppercase;
  }
  .card-back {
    top: 512px;
    background: var(--paper);
  }
  .back-wave {
    position: absolute;
    inset: 0;
    width: 770px;
    height: 440px;
  }
  .back-name {
    position: absolute;
    left: 44px;
    top: 44px;
    color: var(--brand-yellow);
    font-weight: 800;
    font-size: 40px;
    text-transform: uppercase;
    letter-spacing: 0.5px;
  }
  .contact-list {
    position: absolute;
    left: 44px;
    top: 282px;
    list-style: none;
    color: var(--ink);
    font-weight: 500;
    font-size: 19px;
    line-height: 1.6;
  }
  .contact-list li {
    display: flex;
    align-items: center;
    gap: 12px;
  }
  .contact-icon {
    width: 18px;
    height: 18px;
    fill: var(--ink);
    flex: none;
  }
  .tagline {
    position: absolute;
    right: 40px;
    bottom: 30px;
    text-align: right;
    color: var(--ink);
    font-weight: 500;
    font-size: 21px;
    line-height: 1.35;
  }
</style>
</head>
<body>
  <section class="card card-front" aria-label="Card front">
    <h1 class="front-name">Harbor Haul Away</h1>
  </section>

  <section class="card card-back" aria-label="Card back">
    <svg class="back-wave" viewBox="0 0 770 440" aria-hidden="true">
      <path fill="var(--ink)" d="M0,150 C150,130 330,200 470,258 C560,298 680,298 770,225 L770,306 C640,328 540,316 440,284 C300,236 150,170 0,174 Z"/>
      <path fill="var(--brand-yellow)" d="M0,188 C150,182 300,245 450,298 C560,336 680,335 770,320 L770,440 L0,440 Z"/>
    </svg>

    <h2 class="back-name">Harbor Haul Away</h2>

    <ul class="contact-list">
      <li>
        <svg class="contact-icon" viewBox="0 0 24 24"><path d="M6.6 10.8a15 15 0 0 0 6.6 6.6l2.2-2.2a1 1 0 0 1 1-.25 11.4 11.4 0 0 0 3.6.57 1 1 0 0 1 1 1V20a1 1 0 0 1-1 1A17 17 0 0 1 3 4a1 1 0 0 1 1-1h3.5a1 1 0 0 1 1 1c0 1.25.2 2.45.57 3.6a1 1 0 0 1-.25 1z"/></svg>
        555-271-8093
      </li>
      <li>
        <svg class="contact-icon" viewBox="0 0 24 24"><path d="M2 5h20v14H2z M2 5l10 8 10-8" fill="none" stroke="var(--ink)" stroke-width="2"/><path d="M2 5l10 8 10-8z"/></svg>
        www.harborhaulaway.example
      </li>
      <li>
        <svg class="contact-icon" viewBox="0 0 24 24"><circle cx="12" cy="12" r="10"/><path d="M2 12h20M12 2c3 3 3 17 0 20M12 2c-3 3-3 17 0 20" fill="none" stroke="var(--paper)" stroke-width="1.4"/></svg>
        info@harborhaulaway.example
      </li>
    </ul>

    <p class="tagline">Harbor Haul Away<br>Donate - Recycle - Dispose</p>
  </section>
</body>
</html>
```